IT COMPANYcutting edge tec business card

we are IT company that building any apps.
we need business card in japanese and english
You don’t have to include all information in front one you can attach part of that information to back-side
company name : 株式会社ひかりの丘 (BRIGHTHILL Inc.)
concept : cutting-edge technology
role : 取締役 (director)
name : 呉 炫秀 (Oh Hyeonsuk)
post number : 154-0038
address : 東京都世田谷区西若葉台5-14-8 (5-14-8, Nishiwakabadai, Setagaya Ku, Tokyo To, 154-0038, Japan)
Tel:+81-3-5917-2846
Mobile:+81-80-7253-3169
Email : hoh@brighthill-lab.com
website : www.brighthill-lab.com

we dont have logo so please make it as well
we also looking for designer who can make homapage design.

Contact Information for Business Card

cutting-edge design and modern for IT

Font styles to use
Sans Serif

Colors
34a6d7
33b8a4
6092c4
3377b5
886aae
6b449b
b868aa
a64599

Requirements
Must have
• Simple but designed

```html
<!DOCTYPE html>
<html lang="ja">
<head>
<meta charset="utf-8">
<title>BRIGHTHILL Business Card</title>
<link rel="stylesheet" href="https://fonts.googleapis.com/css2?family=Noto+Sans+JP:wght@400;700&family=Quicksand:wght@500&display=swap">
<style>
  :root {
    --bg: #d9d9d9;
    --brand-purple: #69459b;
    --logo-purple: #7b58b0;
    --card-white: #ffffff;
    --text-on-purple: #ffffff;
  }
  html, body {
    margin: 0;
    padding: 0;
    width: 1200px;
    height: 802px;
    overflow: hidden;
    background: var(--bg);
  }
  .canvas {
    position: relative;
    width: 1200px;
    height: 802px;
  }
  .card {
    position: absolute;
    top: 274px;
    width: 442px;
    height: 264px;
    box-shadow: 0 3px 6px rgba(0,0,0,0.35);
    overflow: hidden;
  }
  .card--front {
    left: 136px;
    background: var(--brand-purple);
    color: var(--text-on-purple);
    font-family: "Noto Sans JP", sans-serif;
  }
  .card--back {
    left: 624px;
    background: var(--card-white);
  }
  .person {
    position: absolute;
    left: 15px;
    top: 28px;
  }
  .person__name {
    font-size: 12px;
    font-weight: 700;
    margin: 0;
    letter-spacing: 0.2px;
  }
  .person__name span + span { margin-left: 12px; }
  .person__role {
    font-size: 11.5px;
    margin: 3px 0 0 1px;
  }
  .contact {
    position: absolute;
    left: 15px;
    top: 91px;
    list-style: none;
    margin: 0;
    padding: 0;
    font-size: 11.5px;
    line-height: 15px;
  }
  .contact li {
    display: flex;
    align-items: center;
    gap: 5px;
  }
  .contact svg {
    width: 11px;
    height: 11px;
    fill: var(--text-on-purple);
    flex: none;
  }
  .company {
    position: absolute;
    left: 15px;
    top: 159px;
    font-size: 12px;
    font-weight: 700;
    margin: 0;
  }
  .company span + span { margin-left: 10px; }
  .address {
    position: absolute;
    left: 15px;
    top: 183px;
    font-size: 11.5px;
    line-height: 15px;
    font-style: normal;
  }
  .brand {
    position: absolute;
    left: 0;
    right: 0;
    top: 104px;
    display: flex;
    justify-content: center;
    align-items: center;
    gap: 12px;
    color: var(--logo-purple);
  }
  .brand__dot {
    width: 22px;
    height: 22px;
    border-radius: 50%;
    background: var(--logo-purple);
  }
  .brand__name {
    font-family: "Quicksand", sans-serif;
    font-weight: 500;
    font-size: 36px;
    letter-spacing: 0.5px;
  }
</style>
</head>
<body>
<main class="canvas">
  <section class="card card--front">
    <div class="person">
      <p class="person__name"><span>呉 炫秀</span><span>OH HYEONSUK</span></p>
      <p class="person__role">取締役 Director</p>
    </div>
    <ul class="contact">
      <li>
        <svg viewBox="0 0 12 12" aria-hidden="true"><path d="M1 4c0-2 2-3 5-3s5 1 5 3v1H8.5V4h-5v1H1zM3 6h6l2 4H1z"/></svg>
        +81-3-5917-2846
      </li>
      <li>
        <svg viewBox="0 0 12 12" aria-hidden="true"><path d="M3 0h6v12H3zM4 1.5v8h4v-8z"/></svg>
        +81-80-7253-3169
      </li>
      <li>
        <svg viewBox="0 0 12 12" aria-hidden="true"><path d="M0 2h12v8H0zM1 3l5 4 5-4z" fill-rule="evenodd"/></svg>
        hoh@brighthill-lab.com
      </li>
      <li>
        <svg viewBox="0 0 12 12" aria-hidden="true"><circle cx="6" cy="6" r="5.5"/></svg>
        www.brighthill-lab.com
      </li>
    </ul>
    <p class="company"><span>株式会社ひかりの丘</span><span>BRIGHTHILL</span></p>
    <address class="address">
      東京都世田谷区西若葉台5-14-8<br>
      (5-14-8, Nishiwakabadai<br>
      Setagaya Ku,<br>
      Tokyo To, 154-0038, Japan)
    </address>
  </section>

  <section class="card card--back">
    <div class="brand">
      <span class="brand__dot" aria-hidden="true"></span>
      <span class="brand__name">Brighthill</span>
    </div>
  </section>
</main>
</body>
</html>
```